New Architectural Firm Business Cards

New Business card to compliment previous pixel forum logo (attached). Please design a business card that is simple, modern, creative....please do not use "symbols", simply the logo and associated graphics/text. The front should contain name/address/phone/email/web address (with graphics).....back should be 100% graphic design using the logo somehow. Hoping for a two color (black and yellow) design. full bleed design, no borders

Target Market(s)

Commercial Architecture Clients

Industry/Entity Type

Architecture

Contact Information for Business Card

Please design a business card that is simple, modern, creative....please do not use "symbols", simply the logo and associated graphics/text. The front should contain name/address/phone/email/web address (with graphics).....back should be 100% graphic design using the logo somehow

Font styles to use
Sans Serif

Colors
FFF300
FFF600
FEFA6F
FFFEC7
FFFEE8

Requirements
Must have
• Clean, Modern Design
Should not have
• Stock images or "icons"

```html
<!DOCTYPE html>
<html lang="en">
<head>
<meta charset="utf-8">
<title>Kova Architecture – Business Card</title>
<link href="https://fonts.googleapis.com/css2?family=Rubik:wght@300;400;700&display=swap" rel="stylesheet">
<style>
  :root {
    --page: #dcdcdc;
    --card: #1b1b1b;
    --card-back: #151515;
    --yellow: #f6c216;
    --white: #f4f4f4;
    --grey: #bdbdbd;
    --rule: #a8860f;
    --tone-1: #0c0c0c;
    --tone-2: #242424;
    --tone-3: #363636;
    --tone-4: #545454;
    --tone-5: #767676;
  }
  * { margin: 0; padding: 0; box-sizing: border-box; }
  html, body {
    width: 1087px; height: 1200px; overflow: hidden;
    background: var(--page);
    font-family: "Rubik", sans-serif;
  }
  .card {
    position: absolute; left: 94px;
    width: 900px; height: 514px;
    background: var(--card);
    box-shadow: 0 14px 30px rgba(0,0,0,.28);
    overflow: hidden;
  }
  .card--front { top: 56px; }
  .card--back { top: 630px; background: var(--card-back); }

  .brand {
    position: absolute; left: 82px; top: 52px;
    color: var(--yellow); font-weight: 700;
    line-height: 1;
  }
  .brand__name { font-size: 96px; letter-spacing: -3px; display: block; }
  .brand__line { font-size: 21px; letter-spacing: .5px; display: block; margin-top: 8px; }

  .person { position: absolute; left: 485px; top: 90px; }
  .person__name { color: var(--yellow); font-weight: 700; font-size: 34px; letter-spacing: 1px; }
  .person__role { color: var(--grey); font-weight: 300; font-size: 22px; margin-top: 2px; }

  .rule {
    position: absolute; left: 82px; top: 249px;
    width: 736px; height: 1px; background: var(--rule);
  }

  .contact {
    position: absolute; left: 485px; top: 296px;
    list-style: none; color: var(--white);
    font-weight: 300; font-size: 23px; line-height: 30px;
  }
  .contact li { position: relative; padding-left: 24px; }
  .contact svg { position: absolute; left: 0; top: 8px; width: 15px; height: 15px; fill: var(--yellow); }

  .web {
    position: absolute; left: 82px; top: 416px;
    color: var(--yellow); font-weight: 700; font-size: 23px;
  }

  .pattern {
    position: absolute; left: -62px; top: -52px;
    display: grid;
    grid-template-columns: repeat(7, 158px);
    grid-template-rows: repeat(5, 130px);
  }
  .pattern__mark {
    font-weight: 700; font-size: 58px; letter-spacing: -2px;
    line-height: 130px; text-align: center;
  }
  .t1 { color: var(--tone-1); }
  .t2 { color: var(--tone-2); }
  .t3 { color: var(--tone-3); }
  .t4 { color: var(--tone-4); }
  .t5 { color: var(--tone-5); }
  .accent { color: var(--yellow); }
</style>
</head>
<body>

<section class="card card--front" aria-label="Card front">
  <div class="brand">
    <span class="brand__name">Kova</span>
    <span class="brand__line">ARCHITECTURE</span>
  </div>

  <div class="person">
    <div class="person__name">MARCUS HALE</div>
    <div class="person__role">Manager</div>
  </div>

  <div class="rule"></div>

  <ul class="contact">
    <li>
      <svg viewBox="0 0 16 16" aria-hidden="true"><path d="M8 0a5.5 5.5 0 0 0-5.5 5.5C2.5 10 8 16 8 16s5.5-6 5.5-10.5A5.5 5.5 0 0 0 8 0zm0 7.8a2.3 2.3 0 1 1 0-4.6 2.3 2.3 0 0 1 0 4.6z"/></svg>
      Unit 12 Dockside Yard<br>8 Wren Lane<br>London N4 2QT
    </li>
    <li>
      <svg viewBox="0 0 16 16" aria-hidden="true"><path d="M3.6 0.6 6 3.4 4.6 5.6c.9 2.2 3.3 4.9 5.8 5.9l2.1-1.4 2.9 2.4-1.3 2.7C7.2 15.2.6 8.6 1 1.9z"/></svg>
      +44 (0) 20 7000 4417
    </li>
    <li>
      <svg viewBox="0 0 16 16" aria-hidden="true"><path d="M1 3h14v10H1zM1.8 3.8 8 9l6.2-5.2z" fill-rule="evenodd"/></svg>
      studio@kovaarch.com
    </li>
  </ul>

  <div class="web">kovaarch.com</div>
</section>

<section class="card card--back" aria-label="Card back">
  <div class="pattern" role="img" aria-label="Full-bleed grid of repeated brand names in graded greys with one in yellow">
    <span class="pattern__mark t2">Kova</span><span class="pattern__mark t2">Kova</span><span class="pattern__mark t3">Kova</span><span class="pattern__mark t3">Kova</span><span class="pattern__mark t4">Kova</span><span class="pattern__mark t5">Kova</span><span class="pattern__mark t3">Kova</span>
    <span class="pattern__mark t2">Kova</span><span class="pattern__mark t1">Kova</span><span class="pattern__mark t3">Kova</span><span class="pattern__mark t4">Kova</span><span class="pattern__mark t5">Kova</span><span class="pattern__mark t3">Kova</span><span class="pattern__mark t2">Kova</span>
    <span class="pattern__mark t2">Kova</span><span class="pattern__mark t3">Kova</span><span class="pattern__mark t5">Kova</span><span class="pattern__mark t3">Kova</span><span class="pattern__mark t2">Kova</span><span class="pattern__mark t1">Kova</span><span class="pattern__mark t1">Kova</span>
    <span class="pattern__mark t3">Kova</span><span class="pattern__mark t4">Kova</span><span class="pattern__mark t2">Kova</span><span class="pattern__mark t1">Kova</span><span class="pattern__mark t1">Kova</span><span class="pattern__mark accent">Kova</span><span class="pattern__mark t1">Kova</span>
    <span class="pattern__mark t1">Kova</span><span class="pattern__mark t2">Kova</span><span class="pattern__mark t1">Kova</span><span class="pattern__mark t1">Kova</span><span class="pattern__mark t1">Kova</span><span class="pattern__mark t1">Kova</span><span class="pattern__mark t1">Kova</span>
  </div>
</section>

</body>
</html>
```